design a construction company business card

Design business card around our logo. Card must have all the typical info: name, title, address, phone, email, business name, etc. Somewhere on the card I would like to see our motto "Built on integrity... Inspired by commitment." Consider adding a splash of bright orange to the card to complement the blues and silvers/grays in the logo. We are open to metallic inks, textures, etc. We would like to see options on both light and dark backgrounds. The font in the logo is Euro Technic Extended Regular.

```html
<!DOCTYPE html>
<html lang="en">
<head>
<meta charset="utf-8">
<title>Harlow Contracting – Business Cards</title>
<link href="https://fonts.googleapis.com/css2?family=Open+Sans:wght@400;600;700&family=Michroma&display=swap" rel="stylesheet">
<style>
  :root {
    --page-bg: #d9dbe0;
    --card-light: #ffffff;
    --card-dark: #211f20;
    --brand-blue: #2f63c4;
    --text-light: #f2f2f2;
    --text-muted: #c9c9c9;
    --rule: #ffffff;
  }
  * { box-sizing: border-box; margin: 0; padding: 0; }
  html, body {
    width: 1200px; height: 900px; overflow: hidden;
    background: var(--page-bg);
    font-family: "Open Sans", Arial, sans-serif;
  }
  .sheet {
    position: relative; width: 1200px; height: 900px;
  }
  .card {
    position: absolute; left: 285px; width: 630px; height: 360px;
    box-shadow: 0 6px 18px rgba(0,0,0,0.18);
  }
  .card--front { top: 70px; background: var(--card-light); }
  .card--back { top: 470px; background: var(--card-dark); color: var(--text-light); }

  .brand {
    position: absolute; display: flex; align-items: center; gap: 10px;
    color: var(--brand-blue); font-weight: 700; white-space: nowrap;
  }
  .brand__mark { width: 14px; height: 14px; background: var(--brand-blue); flex: none; }
  .card--front .brand { left: 50%; top: 50%; transform: translate(-50%, -50%); font-size: 30px; }
  .card--back .brand { left: 360px; top: 214px; font-size: 18px; }
  .card--back .brand__mark { width: 10px; height: 10px; }

  .person { position: absolute; left: 44px; top: 36px; }
  .person__name { font-size: 20px; font-weight: 700; }
  .person__title { font-size: 12px; color: var(--text-muted); margin-top: 2px; }

  .contact { position: absolute; left: 44px; top: 112px; font-size: 13px; line-height: 24px; color: var(--text-light); }

  .divider { position: absolute; left: 44px; top: 190px; width: 300px; height: 2px; background: var(--rule); }

  .motto {
    position: absolute; left: 44px; top: 206px; width: 320px;
    font-family: "Michroma", "Open Sans", sans-serif; font-size: 11px;
    color: var(--brand-blue); letter-spacing: 0.5px;
  }
  .address { position: absolute; left: 392px; top: 262px; font-size: 15px; color: var(--text-light); }
</style>
</head>
<body>
  <main class="sheet">
    <section class="card card--front" aria-label="Card front">
      <div class="brand"><span class="brand__mark"></span>Harlow Contracting, Inc.</div>
    </section>

    <section class="card card--back" aria-label="Card back">
      <div class="person">
        <div class="person__name">Your Name</div>
        <div class="person__title">Title</div>
      </div>
      <div class="contact">
        <div class="contact__phone">+99 999 9999</div>
        <div class="contact__email">youremail@website.com</div>
      </div>
      <div class="divider"></div>
      <p class="motto">Built on integrity... Inspired by commitment.</p>
      <div class="brand"><span class="brand__mark"></span>Harlow Contracting, Inc.</div>
      <div class="address">Address location</div>
    </section>
  </main>
</body>
</html>
```